Rusty Clem's BBQ is an online seasoning and other food sales business.

I need a website and store to launch this new business. The site must be compatible to smart phones. Most of the marketing will be done through short comedic social media videos that are unrelated to cooking for entertainment purposes. I will also have cooking instructional videos. I will sell merchandise in the future. Products for sale now will be my Beef Rub and Pork Rub. In 2 months I will have an All Seasoning and Cajun Seasoning. Later this year I will add Rusty Clem's Ranch Beans and a BBQ sauce along with merchandise. I have a logo and labels designs for the seasonings. I will upload pictures of the bottles soon. I do not want this to look like a generic BBQ website because my products are not inclusive to smoking meat. No pigs or cartoon pictures on my website besides my logo. Stock photos of brisket, pork butt, ribs and chicken are welcome. The company is fun and entertaining unlike any seasoning in this world. We will make you laugh and happy through our products and videos. I had to use Rusty Clem's BBQ name due to trademark issue. Rusty Clem's is already trademarked. I'm trademarking Rusty Clem's BBQ. I'm not a huge fan of the BBQ part because it may deter some people from buying the product thinking it only for smoking meat. The roots of my company came from smoking delicious meets as a hobby and small catering jobs. I want people to use this on everything from eggs to soups, stews, vegetables, pastas, beans and many more side dishes. If you eat meat prepared in any way, these seasonings are for you. I'm more than happy to get you other pictures of meat and add content as required. I'm just setting up this company and will get you the required information upon request. I attached a sample of a blue and green label for the All Seasoning which is not finalized yet. I will use the blue label version with updated nutrient facts and ingredients.

```html
<!DOCTYPE html>
<html lang="en">
<head>
<meta charset="utf-8">
<title>Rusty Clem's BBQ</title>
<link href="https://fonts.googleapis.com/css2?family=Outfit:wght@400;500;600;700&display=swap" rel="stylesheet">
<style>
:root{
  --accent:#f0401f;
  --blue:#1552bd;
  --ink:#111111;
  --muted:#444444;
  --panel:#f2f2f2;
  --card:#f4f4f4;
  --star:#f5a31a;
  --white:#ffffff;
  --footer:#121212;
}
*{box-sizing:border-box;margin:0;padding:0}
html,body{width:1200px;height:3981px;overflow:hidden}
body{position:relative;background:var(--white);font-family:'Outfit',sans-serif;color:var(--ink)}
.abs{position:absolute}
.btn{position:absolute;display:flex;align-items:center;justify-content:center;border-radius:30px;color:var(--white);font-size:13px;font-weight:500;background:var(--accent)}
.btn.blue{background:var(--blue)}
.photo{position:absolute;overflow:hidden}
h2{position:absolute;left:0;width:1200px;text-align:center;font-size:37px;font-weight:600;letter-spacing:-1px;line-height:45px}

/* hero */
.hero{position:absolute;left:0;top:0;width:1200px;height:810px;
  background:
    radial-gradient(ellipse 250px 230px at 610px 330px,#5a2418 0%,#3e1c14 55%,rgba(62,28,20,0) 100%),
    radial-gradient(ellipse 720px 360px at 600px 520px,#b89880 0%,#8a6a58 40%,#3a2a24 72%,#151114 100%)}
.nav{position:absolute;left:105px;top:39px;width:990px;height:77px;border:1.5px solid rgba(255,255,255,.85);border-radius:40px}
.nav-links{position:absolute;left:52px;top:0;height:77px;display:flex;align-items:center;gap:27px;color:var(--white);font-size:13px}
.brand{position:absolute;display:flex;align-items:center;justify-content:center;gap:8px;font-weight:700;white-space:nowrap}
.brand .dot{width:20px;height:20px;border-radius:50%;background:#f7c51c;flex:none}
.hero .brand{left:450px;top:62px;width:300px;font-size:21px;color:var(--white)}
.social{position:absolute;width:40px;height:40px;border:1.5px solid rgba(255,255,255,.8);border-radius:50%;display:flex;align-items:center;justify-content:center}
.thumb{position:absolute;width:88px;height:88px;border-radius:50%;border:3px solid rgba(255,255,255,.75)}
.hero-title{position:absolute;left:105px;top:624px;color:var(--white);font-size:51px;font-weight:700;letter-spacing:-1.8px;line-height:60px}

/* flavor */
.card-title{position:absolute;width:388px;text-align:center;font-size:21px;font-weight:600;letter-spacing:-.4px}
.card-desc{position:absolute;width:388px;text-align:center;font-size:12px;line-height:18px;color:var(--muted)}
.rule{position:absolute;left:131px;top:1299px;width:939px;height:1px;background:#cfcfcf}

/* about */
.about-h{position:absolute;left:496px;top:1402px;font-size:37px;font-weight:600;letter-spacing:-1px;line-height:41px}
.about-p{position:absolute;left:496px;width:368px;font-size:11.5px;line-height:18.5px;color:var(--muted)}

/* uses */
.uses{position:absolute;left:0;top:1813px;width:1200px;height:444px;background:var(--panel)}
.use{position:absolute;width:142px;text-align:center}
.use .circle{width:142px;height:142px;border-radius:50%}
.use span{display:block;margin-top:12px;font-size:15px;font-weight:600}

/* video */
.sub{position:absolute;left:0;width:1200px;text-align:center;font-size:12px;line-height:18px;color:var(--muted)}
.play{position:absolute;left:552px;top:2651px;width:96px;height:96px;border-radius:50%;background:var(--accent)}

/* reviews */
.review{position:absolute;top:3076px;height:174px;background:var(--card);border-radius:14px;padding:26px 20px 0 20px}
.stars{display:flex;gap:2px;margin-bottom:9px}
.review p{font-size:11.5px;line-height:18.5px;color:var(--muted)}
.review b{display:block;margin-top:9px;font-size:12px;font-weight:600;color:var(--ink)}
.dots{position:absolute;left:580px;top:3279px;display:flex;gap:5px}
.dots i{width:8px;height:8px;border-radius:50%;background:#cfcfcf}
.dots i.on{background:var(--ink)}

/* newsletter */
.signup{position:absolute;left:263px;top:3451px;width:669px;height:48px;border-radius:26px;background:var(--card)}
.signup .field{position:absolute;left:52px;top:15px;font-size:12px;color:var(--muted)}

/* footer */
.footer{position:absolute;left:0;top:3593px;width:1200px;height:388px;background:var(--footer);color:var(--white)}
.footer .brand{left:420px;top:100px;width:360px;font-size:24px}
.foot-links{position:absolute;left:0;top:208px;width:1200px;display:flex;justify-content:center;gap:54px;font-size:13px}
.foot-social{position:absolute;width:38px;height:38px;border:1.5px solid rgba(255,255,255,.7);border-radius:50%;top:248px;display:flex;align-items:center;justify-content:center}
.foot-rule{position:absolute;left:105px;top:314px;width:990px;height:1px;background:#3a3a3a}
.copy{position:absolute;left:0;top:348px;width:1200px;text-align:center;font-size:12px}
</style>
</head>
<body>

<section class="hero" role="img" aria-label="Plated seared steak with glaze, cherry tomatoes and greens, held on a plate">
  <nav class="nav">
    <div class="nav-links"><span>Home</span><span>Shop</span><span>Recipes</span><span>Videos</span><span>About Us</span></div>
    <span class="social" style="left:705px;top:18px" aria-label="Share">
      <svg width="16" height="16" viewBox="0 0 16 16" fill="none" stroke="#fff" stroke-width="1.4"><circle cx="12" cy="3.5" r="2"/><circle cx="4" cy="8" r="2"/><circle cx="12" cy="12.5" r="2"/><path d="M5.8 7 10.2 4.5M5.8 9l4.4 2.5"/></svg>
    </span>
    <span class="social" style="left:755px;top:18px" aria-label="Messages">
      <svg width="16" height="16" viewBox="0 0 16 16" fill="none" stroke="#fff" stroke-width="1.4"><path d="M2 3h12v8H6l-3 3v-3H2z"/></svg>
    </span>
    <span class="btn" style="left:809px;top:16px;width:162px;height:45px">Shop Seasonings</span>
  </nav>
  <div class="brand"><span class="dot"></span>Rusty Clem's BBQ</div>
  <div class="thumb" style="left:1006px;top:245px;background:#c87a4a" role="img" aria-label="Salmon dish"></div>
  <div class="thumb" style="left:1006px;top:341px;background:#6a3024" role="img" aria-label="Steak dish"></div>
  <div class="thumb" style="left:1006px;top:437px;background:#c8602c" role="img" aria-label="Chicken dish"></div>
  <h1 class="hero-title">Seasoning So Good<br>You'll Put It On Everything.</h1>
  <span class="btn" style="left:839px;top:665px;width:115px;height:47px">Shop Rubs</span>
  <span class="btn blue" style="left:962px;top:665px;width:133px;height:47px">Watch Videos</span>
</section>

<h2 style="top:891px">Flavor Starts Here</h2>
<div class="photo" style="left:201px;top:957px;width:388px;height:207px;border-radius:14px;background:linear-gradient(120deg,#3a2c26 0%,#6a3a26 45%,#c8803e 100%)" role="img" aria-label="Sliced seasoned beef on a cutting board"></div>
<div class="photo" style="left:611px;top:957px;width:388px;height:207px;border-radius:14px;background:linear-gradient(120deg,#cfc6bc 0%,#e2dcd6 40%,#c65a20 60%,#e0d8d0 100%)" role="img" aria-label="Pork rub spice in a white scoop"></div>
<div class="card-title" style="left:201px;top:1176px">Beef Rub</div>
<div class="card-title" style="left:611px;top:1176px">Pork Rub</div>
<p class="card-desc" style="left:201px;top:1204px">Bold, savory flavor made for steaks, burgers,<br>brisket, and more.</p>
<p class="card-desc" style="left:611px;top:1204px">Sweet heat and smoky goodness perfect for<br>ribs, pulled pork.</p>
<div class="rule"></div>

<div class="photo" style="left:119px;top:1374px;width:332px;height:347px;border-radius:14px;background:linear-gradient(160deg,#b8a898 0%,#8a7060 55%,#6a7448 100%)" role="img" aria-label="Two people cooking together in a kitchen"></div>
<h3 class="about-h">Not Your Average<br>BBQ Brand.</h3>
<p class="about-p" style="top:1495px">We don't just sell seasoning — we bring energy, flavor, and fun back into your kitchen. Every shake is designed to turn ordinary meals into something exciting, bold, and worth talking about.</p>
<p class="about-p" style="top:1564px">From quick weekday breakfasts to weekend cookouts with friends, our blends fit every moment where food meets mood. No rules, no limits — just real flavor that works on everything you cook.</p>
<span class="btn" style="left:496px;top:1640px;width:120px;height:45px">Read More</span>
<div class="photo" style="left:911px;top:1527px;width:170px;height:194px;border-radius:14px;background:linear-gradient(160deg,#7a8a76 0%,#a89a88 50%,#4a4646 100%)" role="img" aria-label="Friends at an outdoor grill cookout"></div>

<section class="uses">
  <h2 style="top:58px">Made For More Than BBQ</h2>
  <div class="use" style="left:125px;top:124px"><div class="circle" style="background:radial-gradient(circle,#f2ece4 32%,#9a6a3a 78%)" role="img" aria-label="Bowl of eggs"></div><span>Eggs</span></div>
  <div class="use" style="left:286px;top:124px"><div class="circle" style="background:radial-gradient(circle,#e88a2a 32%,#b07a5a 78%)" role="img" aria-label="Bowl of soup"></div><span>Soups</span></div>
  <div class="use" style="left:447px;top:124px"><div class="circle" style="background:radial-gradient(circle,#e8703a 32%,#5a4a3a 78%)" role="img" aria-label="Plate of pasta"></div><span>Pasta</span></div>
  <div class="use" style="left:608px;top:124px"><div class="circle" style="background:radial-gradient(circle,#d8803a 32%,#7a7a7a 78%)" role="img" aria-label="Fried chicken"></div><span>Chicken</span></div>
  <div class="use" style="left:768px;top:124px"><div class="circle" style="background:radial-gradient(circle,#6a2a1e 38%,#c8b8a8 80%)" role="img" aria-label="Bowl of beans"></div><span>Beans</span></div>
  <div class="use" style="left:929px;top:124px"><div class="circle" style="background:radial-gradient(circle,#f0a030 28%,#3a3a3a 72%)" role="img" aria-label="Cup of fries"></div><span>Fries</span></div>
  <span class="btn" style="left:540px;top:330px;width:120px;height:46px">View More</span>
</section>

<h2 style="top:2342px">Come For The Laughs. Stay<br>For The Flavor.</h2>
<p class="sub" style="top:2440px">Watch hilarious content, cooking tips, recipes, backyard experiments, and flavor-packed<br>creations from Rusty Clem's BBQ.</p>
<div class="photo" style="left:190px;top:2504px;width:820px;height:390px;border-radius:30px;background:linear-gradient(135deg,#d8dadc 0%,#c4c6c8 45%,#8a8680 78%,#c05a3a 100%)" role="img" aria-label="Video still of a cook chopping vegetables in a bright kitchen"></div>
<div class="play"><svg width="96" height="96" viewBox="0 0 96 96"><path d="M42 36 L60 48 L42 60 Z" fill="#fff"/></svg></div>

<h2 style="top:2963px">People Are Putting This Stuff<br>On Everything.</h2>
<div class="review" style="left:144px;width:292px">
  <div class="stars"><svg width="76" height="13" viewBox="0 0 76 13"><g fill="#f5a31a"><path id="s" d="M6.5 0l1.9 4.2 4.6.5-3.4 3.1 1 4.5-4.1-2.4-4.1 2.4 1-4.5L0 4.7l4.6-.5z"/><use href="#s" x="15.5"/><use href="#s" x="31"/><use href="#s" x="46.5"/><use href="#s" x="62"/></g></svg></div>
  <p>"This beef rub completely changed the way I make burgers at home. I didn't expect that much flavor from a dry rub, but now I literally can't cook burgers without it."</p><b>John Smith</b>
</div>
<div class="review" style="left:453px;width:294px">
  <div class="stars"><svg width="76" height="13" viewBox="0 0 76 13"><g fill="#f5a31a"><use href="#s"/><use href="#s" x="15.5"/><use href="#s" x="31"/><use href="#s" x="46.5"/><use href="#s" x="62"/></g></svg></div>
  <p>"Honestly the best seasoning I've used on chicken. Whether it's grilled, baked, or pan-fried, it brings out a flavor I didn't know was missing before."</p><b>Sara John</b>
</div>
<div class="review" style="left:764px;width:292px">
  <div class="stars"><svg width="76" height="13" viewBox="0 0 76 13"><g fill="#f5a31a"><use href="#s"/><use href="#s" x="15.5"/><use href="#s" x="31"/><use href="#s" x="46.5"/><use href="#s" x="62"/></g></svg></div>
  <p>"I've used it on steak, fries, and even roasted vegetables — it works on everything. One of those rare seasonings you keep reaching for without thinking."</p><b>Sara John</b>
</div>
<div class="dots"><i></i><i class="on"></i><i></i></div>

<h2 style="top:3357px">Join The Flavor Crew</h2>
<p class="sub" style="top:3408px">Get new product drops, funny videos, recipes, &amp; exclusive deals delivered straight to your inbox.</p>
<div class="signup">
  <svg class="abs" style="left:30px;top:18px" width="14" height="11" viewBox="0 0 14 11"><rect width="14" height="11" rx="1.5" fill="#1552bd"/><path d="M1 1.5 L7 6 L13 1.5" stroke="#fff" stroke-width="1.3" fill="none"/></svg>
  <span class="field">Email Address...</span>
  <span class="btn" style="left:527px;top:0;width:142px;height:48px">Subscribe Now</span>
</div>

<footer class="footer">
  <div class="brand"><span class="dot"></span>Rusty Clem's BBQ</div>
  <div class="foot-links"><span>Home</span><span>Shop</span><span>Recipes</span><span>Videos</span><span>About Us</span><span>Contact Us</span></div>
  <span class="foot-social" style="left:513px" aria-label="Share">
    <svg width="14" height="14" viewBox="0 0 16 16" fill="none" stroke="#fff" stroke-width="1.4"><circle cx="12" cy="3.5" r="2"/><circle cx="4" cy="8" r="2"/><circle cx="12" cy="12.5" r="2"/><path d="M5.8 7 10.2 4.5M5.8 9l4.4 2.5"/></svg>
  </span>
  <span class="foot-social" style="left:558px" aria-label="Messages">
    <svg width="14" height="14" viewBox="0 0 16 16" fill="none" stroke="#fff" stroke-width="1.4"><path d="M2 3h12v8H6l-3 3v-3H2z"/></svg>
  </span>
  <span class="foot-social" style="left:603px" aria-label="Email">
    <svg width="14" height="14" viewBox="0 0 16 16" fill="none" stroke="#fff" stroke-width="1.4"><rect x="1.5" y="3.5" width="13" height="9" rx="1"/><path d="M2 4l6 4.5L14 4"/></svg>
  </span>
  <span class="foot-social" style="left:648px" aria-label="Website">
    <svg width="14" height="14" viewBox="0 0 16 16" fill="none" stroke="#fff" stroke-width="1.4"><circle cx="8" cy="8" r="6.2"/><path d="M1.8 8h12.4M8 1.8c2.2 2.4 2.2 10 0 12.4M8 1.8c-2.2 2.4-2.2 10 0 12.4"/></svg>
  </span>
  <div class="foot-rule"></div>
  <p class="copy">© 2026 Rusty Clem's BBQ. All Rights Reserved.</p>
</footer>

</body>
</html>
```